NZ First of it's kind solutions directory and marketplace for busy Mums needs a business card design

We need a business card design for our new nationwide business in NZ (long term plans to go global). We provide solutions to the everyday challenges that busy Mums face by connecting them with quality communities and suppliers of carefully selected, relevant products and services. We sell direct via our online marketplace. The final design should communicate our values of inclusivity, quality and smart solutions. Colours should incorporate our logo colour palette of #477077 and #6ba8b2. Our website is at https://www.brightnestly.com

Target Market(s)

busy Mums, Age 28 – 50, female, income over $100K, location main centres NZ primarily but NZ wide. Is likely juggling work or career with a young family. Probably had hobbies which have fallen by the wayside.
-Wants to succeed in her chosen career without compromising on family life
-to successfully juggle her career without feeling like she is compromising her children
- Is time poor, something always has to give and it’s generally her health (she’ll stay up late, get stressed)
- probably ex corporate or professional career. Has discretional income

Industry/Entity Type

Business

Contact Information for Business Card

Jodie Farnsworth, Founder, BrightNestly.com (Strapline Browse; Pick; Sorted), 48 Kowhai Terrace, Hillsborough, Auckland 1058, New Zealand. Mob: 021 437 518 Ph: +64 (0)9 584 7163

Font styles to use
Other font styles liked:
• Raleway, and/or Architects Daughter

Colors
00a990
33b8a4
86cfc6
cfeae6

Requirements
Must have
• the above details, streamline. the logo and colours associated with those logos
Should not have
• foil or metallic colours

```html
<!DOCTYPE html>
<html lang="en">
<head>
<meta charset="utf-8">
<title>BrightNestly – Business Card</title>
<link href="https://fonts.googleapis.com/css2?family=Architects+Daughter&family=Raleway:wght@500;600;700&display=swap" rel="stylesheet">
<style>
  :root {
    --backdrop: #1b1d1c;
    --paper: #ffffff;
    --teal-dark: #477077;
    --teal-light: #6ba8b2;
    --ink: #5a5f61;
  }
  * { box-sizing: border-box; margin: 0; padding: 0; }
  html, body {
    width: 1200px; height: 1000px; overflow: hidden;
    background: var(--backdrop);
    font-family: "Raleway", sans-serif;
  }
  .sheet {
    position: relative; width: 1200px; height: 1000px;
    display: flex; flex-direction: column; align-items: center; justify-content: center; gap: 50px;
  }
  .card {
    position: relative; width: 720px; height: 410px;
    background: var(--paper); border-radius: 22px; overflow: hidden;
  }
  .card-art { position: absolute; inset: 0; width: 100%; height: 100%; }

  /* Front */
  .brand {
    position: absolute; left: 0; right: 0; top: 52px;
    display: flex; flex-direction: column; align-items: center;
  }
  .brand-row { display: flex; align-items: center; gap: 16px; }
  .brand-dot { width: 42px; height: 42px; border-radius: 50%; background: var(--teal-dark); }
  .brand-name {
    font-weight: 700; font-size: 56px; color: var(--teal-dark); letter-spacing: -0.5px; line-height: 1;
  }
  .strapline {
    margin-top: 8px; margin-left: 58px;
    font-family: "Architects Daughter", cursive; font-size: 26px; color: #3f4446; letter-spacing: 1px;
  }
  .website {
    position: absolute; left: 0; right: 0; bottom: 34px; text-align: center;
    font-weight: 700; font-size: 26px; color: var(--paper); letter-spacing: 4px;
  }

  /* Back */
  .holder-name {
    position: absolute; left: 44px; top: 40px;
    font-weight: 700; font-size: 38px; color: #3b5c62; letter-spacing: 0.5px;
  }
  .holder-role {
    position: absolute; right: 48px; top: 168px;
    font-weight: 600; font-size: 18px; color: var(--paper); letter-spacing: 3px;
  }
  .contact {
    position: absolute; left: 44px; bottom: 56px;
    font-weight: 500; font-size: 21px; color: var(--ink); line-height: 1.3;
  }
  .divider {
    position: absolute; left: 300px; bottom: 34px; width: 3px; height: 80px; background: var(--ink);
  }
  .address {
    position: absolute; left: 330px; bottom: 30px;
    font-weight: 500; font-size: 21px; color: var(--ink); line-height: 1.3;
  }
</style>
</head>
<body>
<main class="sheet">

  <section class="card card-front">
    <svg class="card-art" viewBox="0 0 720 410" preserveAspectRatio="none" aria-hidden="true">
      <path d="M0,205 C150,125 330,170 470,250 C570,305 650,300 720,270 L720,410 L0,410 Z" fill="var(--teal-dark)"/>
      <path d="M40,180 C170,150 300,170 400,225 C300,185 170,170 40,190 Z" fill="var(--paper)"/>
      <path d="M420,245 C560,300 650,285 720,240 L720,262 C650,300 560,312 420,245 Z" fill="var(--teal-light)"/>
      <path d="M420,245 C560,312 650,300 720,262 L720,270 C650,308 560,318 420,250 Z" fill="var(--paper)"/>
    </svg>
    <div class="brand">
      <div class="brand-row">
        <span class="brand-dot"></span>
        <span class="brand-name">BrightNestly</span>
      </div>
      <p class="strapline">Browse - Pick - Sorted</p>
    </div>
    <p class="website">www.brightnestly.com</p>
  </section>

  <section class="card card-back">
    <svg class="card-art" viewBox="0 0 720 410" preserveAspectRatio="none" aria-hidden="true">
      <path d="M0,0 H720 V285 C640,225 570,205 480,210 C340,218 150,195 0,120 Z" fill="var(--teal-light)"/>
      <path d="M0,150 C140,210 290,238 420,240 C290,252 140,238 0,178 Z" fill="var(--teal-light)"/>
      <path d="M490,214 C610,222 690,290 720,360 V300 C680,250 600,220 490,214 Z" fill="var(--teal-dark)"/>
    </svg>
    <h1 class="holder-name">JODIE FARNSWORTH</h1>
    <p class="holder-role">FOUNDER</p>
    <p class="contact">Mob: 021 437 518<br>Ph: +64 (0)9 584 7163</p>
    <span class="divider"></span>
    <p class="address">48 Kowhai Terrace, Hillsborough<br>Auckland 1058, New Zealand</p>
  </section>

</main>
</body>
</html>
```